Web Design Project - Cosmetic Medispa

Our client's current website www.brightvellora.com.au needs a major overhaul. We need a template for the Home page and an Inner/procedure page.
Their main audience is women 25-55.
The website navigation is as per the attached Word document.
Scrolling animation needed in the header section (we will animate the photo), with the words “Vellora care you can rely on” neatly over the top of the image.
The footer of the website needs to contain links to all their procedures per the attached word document (see the bottom part of the document).
“Virtual Consultation” button/icon/banner needed on Home page.
"Vellora Answer Locator" button/icon/banner needed on Home page (this is a tool that lets visitors search for problems (e.g. wrinkles) and it provides a solution (e.g. 'botox').
Add a “Subscribe for Specials” box to all pages.
Colour scheme to be along the lines of that used in the attached Marnio images.
Home page must use the following images that are attached (flipped yellow bikini, sarong, and doctor).

```html
<!DOCTYPE html>
<html lang="en">
<head>
<meta charset="utf-8">
<title>Vellora Cosmetic Medicine – Home</title>
<link href="https://fonts.googleapis.com/css2?family=Merriweather:wght@400;700&family=Delius&display=swap" rel="stylesheet">
<style>
  :root {
    --bg-dark: #2e1e0f;
    --bg-mid: #4a3420;
    --gold: #c9a66b;
    --gold-light: #f1dba4;
    --cream: #f5e6c4;
    --tab-active: #6f5230;
    --btn-top: #6e5333;
    --btn-bottom: #4a331b;
    --sky-top: #6aa6e4;
    --sky-bottom: #8dbcea;
    --divider: #241709;
    --social-blue: #3b5998;
  }
  * { box-sizing: border-box; margin: 0; padding: 0; }
  html, body { width: 1200px; height: 900px; overflow: hidden; }
  body {
    position: relative;
    background: radial-gradient(ellipse 700px 600px at 600px 420px, var(--bg-mid), var(--bg-dark));
    font-family: "Merriweather", Georgia, serif;
    color: var(--cream);
  }

  .brand {
    position: absolute; left: 100px; top: 26px; width: 140px;
    text-align: center; color: var(--gold);
    font-family: "Merriweather", Georgia, serif; font-weight: 400;
  }
  .brand-mark { display: block; width: 52px; height: 52px; margin: 0 auto 10px; border-radius: 50%; background: var(--gold); }
  .brand-name { display: block; font-size: 24px; letter-spacing: 1px; line-height: 26px; }
  .brand-sub { display: block; font-size: 8px; letter-spacing: 1.6px; }

  .main-nav { position: absolute; left: 271px; top: 0; height: 126px; display: flex; }
  .main-nav a {
    display: block; height: 126px; padding: 101px 0 0;
    font-family: "Delius", cursive; font-size: 15px; color: var(--gold);
    text-decoration: none; text-shadow: 0 1px 2px #000;
  }
  .main-nav a.active { width: 95px; background: var(--tab-active); color: #2e1d0c; text-align: center; text-shadow: none; }
  .nav-about { margin-left: 28px; }
  .nav-procedures { margin-left: 57px; }
  .nav-specials { margin-left: 54px; }
  .nav-shop { margin-left: 59px; }
  .nav-media { margin-left: 58px; }
  .nav-contact { margin-left: 56px; }

  .tagline {
    position: absolute; left: 0; width: 1200px; top: 152px; text-align: center;
    font-size: 24px; font-weight: 700; color: var(--gold); text-shadow: 1px 2px 2px #120a02;
  }
  .social-badge {
    position: absolute; left: 956px; top: 143px; width: 144px; height: 44px;
    background: #f1f3f7; border: 1px solid #c7ccd6; display: flex; align-items: center;
    gap: 8px; padding-left: 7px; color: var(--social-blue); font-size: 12px; font-weight: 700;
    line-height: 15px; text-decoration: none;
  }
  .social-badge .sq { width: 30px; height: 30px; background: var(--social-blue); flex: none; }

  .hero {
    position: absolute; left: 100px; top: 200px; width: 1000px; height: 389px;
    background: linear-gradient(180deg, var(--sky-top), var(--sky-bottom));
    box-shadow: 0 2px 4px rgba(0,0,0,.5);
  }
  .slide-arrow { position: absolute; top: 175px; width: 32px; height: 32px; }
  .slide-arrow.prev { left: 25px; }
  .slide-arrow.next { right: 25px; }

  .mission { position: absolute; left: 100px; top: 612px; width: 728px; }
  .mission h1 { font-size: 20px; font-weight: 700; color: var(--gold-light); margin-bottom: 2px; }
  .mission p { font-size: 11.3px; letter-spacing: 0.45px; line-height: 17.4px; margin-bottom: 15.4px; }

  .column-divider { position: absolute; left: 835px; top: 604px; width: 3px; height: 296px; background: var(--divider); }

  .sidebar { position: absolute; left: 850px; top: 610px; width: 250px; }
  .subscribe-bar {
    height: 34px; padding: 8px 10px; font-size: 14px; color: var(--gold-light);
    background: linear-gradient(180deg, var(--btn-top), var(--btn-bottom));
    box-shadow: 0 1px 3px rgba(0,0,0,.6);
  }
  .subscribe-info { margin-top: 8px; font-size: 10.5px; font-weight: 700; line-height: 16px; color: var(--gold-light); }
  .side-button {
    display: block; height: 44px; margin-top: 11px; text-align: center; line-height: 44px;
    font-size: 14px; font-weight: 700; color: var(--gold-light); text-decoration: none;
    background: linear-gradient(180deg, var(--btn-top), var(--btn-bottom));
    border: 1px solid #2b1c0c; box-shadow: 0 1px 3px rgba(0,0,0,.6);
  }
  .side-button.first { margin-top: 42px; }
  .free-consult { margin-top: 24px; font-size: 17px; line-height: 23px; color: var(--gold-light); }
</style>
</head>
<body>
  <header>
    <div class="brand">
      <span class="brand-mark"></span>
      <span class="brand-name">VELLORA</span>
      <span class="brand-sub">COSMETIC MEDICINE</span>
    </div>
    <nav class="main-nav">
      <a href="#" class="active">Home</a>
      <a href="#" class="nav-about">About</a>
      <a href="#" class="nav-procedures">Procedures</a>
      <a href="#" class="nav-specials">Specials</a>
      <a href="#" class="nav-shop">Shop</a>
      <a href="#" class="nav-media">Media</a>
      <a href="#" class="nav-contact">Contact</a>
    </nav>
    <h2 class="tagline">Vellora care you can rely on</h2>
    <a class="social-badge" href="#"><span class="sq"></span><span>Find us on<br>Linkvale</span></a>
  </header>

  <section class="hero" role="img" aria-label="Header photo: woman seen from behind against a clear blue sky">
    <svg class="slide-arrow prev" viewBox="0 0 32 32" aria-hidden="true">
      <circle cx="16" cy="16" r="15" fill="#f4f4f4" stroke="#bbb"/>
      <path d="M18 10 L12 16 L18 22" fill="none" stroke="#333" stroke-width="3"/>
    </svg>
    <svg class="slide-arrow next" viewBox="0 0 32 32" aria-hidden="true">
      <circle cx="16" cy="16" r="15" fill="#f4f4f4" stroke="#bbb"/>
      <path d="M14 10 L20 16 L14 22" fill="none" stroke="#333" stroke-width="3"/>
    </svg>
  </section>

  <main class="mission">
    <h1>Mission Statement</h1>
    <p>At Vellora Cosmetic Medicine it is our main objective to match the correct procedure with the correct patient and deliver a high standard of care to make Cosmetic Medicine a happy experience and not one to be feared. We firmly believe that patients should not rush into unwanted procedures, but should dip their toe in at the lower risk end of the cosmetic pool and receive guidance from our caring staff.</p>
    <p>As well as providing a comfortable and friendly approach to Cosmetic Medicine, we also believe our treatments should be accessible to all areas of Western Australia. Based in Ashvale, not far from Perth’s city centre, we also now have a long list of outer metro and country clinics to ensure excellent availability across the state. We can provide our cosmetic surgery procedures in Perth and 7 additional regional locations.</p>
    <p>All of our practitioners and cosmetic surgeons have been stringently selected by Dr Halden for their experience, expertise and caring nature, ensuring all of our treatments are given to the highest standard in a friendly environment. We also believe you should be able to receive excellent advice before you start your journey of improvement, and as such we provide complimentary and non-obligation consultations to help you decide which of our many cosmetic treatments is right for you. Cosmetic Surgery Benefits The Benefits of Vellora for your Cosmetic Surgery &amp; Non-Surgical Procedures include:</p>
  </main>

  <div class="column-divider"></div>

  <aside class="sidebar">
    <div class="subscribe-bar">Subscribe for Specials!</div>
    <p class="subscribe-info">Call Now: (08) 9471 2260<br>Click here to Subscribe to Our Newsletter</p>
    <a href="#" class="side-button first">Virtual Consultation</a>
    <a href="#" class="side-button">Vellora Answer Locator</a>
    <p class="free-consult">Book a FREE 30<br>Minute Consultation</p>
  </aside>
</body>
</html>
```